Bright Thrift needs a web design and brand identifier

Bright Thrift is a pioneering approach by Victorian councils and four greenhouse alliances to support low income households to install solar systems with no upfront costs.

Bright Thrift will commence in May 2017.

Bright Thrift is looking for a designer to create a website banner incorporating a brand identifier for Bright Thrift. The brand identifier will be used in Bright Thrift promotional materials, such as flyers and mail outs.

The website banner and brand identifier should engender trust and confidence in the target group (retirees).
Updates

Reason: Hi, Thank you for your work so far. We've been given advice to get a separate logo designed (instead of trying to include this as part of the banner design). Sorry for not realising this until now - we're new to all this. So, I have a couple of preliminary logo designs that are being considered by our project control group. I will forward a copy of the logo once we have it. The project control group is looking for a web design that is unique to Bright Thrift and a design that draws on the key elements of the program (i.e. it helps people save money and take control). The site should be friendly but not too informal as the target group is seniors. Here's a link to another community energy organisation: www.kindlecurrent.com.au/ Apologies again for the delays. Cheers, Ned

Target Market(s)

Home owning, low income, retirees

Industry/Entity Type

Non Profit

Number of Pages Required

1 page

Font styles to use
Sans Serif

Requirements
Must have
• Use of Bright Thrift name
• Must promote Bright Thrift as safe, reliable and trustworthy
Nice to have
• Blue - to engender sense of safety and confidence (open to suggestions, though)
• Solar panels / the sun
Should not have
• Anything that is hard to read
• anything that promotes riskyness

```html
<!DOCTYPE html>
<html lang="en">
<head>
<meta charset="utf-8">
<title>Bright Thrift</title>
<link href="https://fonts.googleapis.com/css2?family=Roboto:wght@300;400;500;700&display=swap" rel="stylesheet">
<style>
:root{
  --blue:#3f6fd1;
  --blue-light:#5b8ce0;
  --blue-dark:#2f5cb8;
  --orange:#f7941d;
  --ink:#333333;
  --muted:#666666;
  --gray-bg:#f3f3f3;
  --line:#dddddd;
  --dark:#1d2230;
  --white:#ffffff;
}
*{margin:0;padding:0;box-sizing:border-box}
html,body{width:1200px;height:3888px;overflow:hidden}
body{position:relative;font-family:'Roboto',sans-serif;color:var(--ink);background:var(--white)}
.abs{position:absolute}
p{font-size:12px;line-height:19px;color:var(--muted)}

/* header */
.phone-tab{left:920px;top:0;width:252px;height:36px;background:var(--blue);border-radius:0 0 0 26px;color:var(--white);font-size:14px;display:flex;align-items:center;justify-content:center;gap:10px}
.logo{left:98px;top:34px;display:flex;align-items:center;gap:12px}
.logo-dot{width:44px;height:44px;border-radius:50%;background:var(--orange)}
.logo-name{font-size:30px;font-weight:700;color:var(--blue);text-transform:uppercase;letter-spacing:.5px}
.nav{left:500px;top:52px;display:flex;align-items:center;gap:0}
.nav a{font-size:12px;color:var(--ink);text-decoration:none;text-transform:uppercase;height:36px;display:flex;align-items:center}
.nav a.active{background:var(--orange);color:var(--white);border-radius:18px;width:80px;justify-content:center;font-weight:500}

/* hero */
.hero{left:0;top:109px;width:1200px;height:448px;background:linear-gradient(180deg,#6f9fe0 0%,#a9c9ef 45%,#8bbf5a 62%,#5f9a32 100%)}
.hero-panels{left:0;top:109px;width:650px;height:448px;background:linear-gradient(135deg,#243a6e,#3f6ab8 60%,#9fbbe0);clip-path:polygon(0 0,55% 0,100% 100%,0 100%)}
.hero-cut{left:0;top:109px}
.hero-title{left:783px;top:280px;font-size:46px;font-weight:500;color:var(--white);text-transform:uppercase}
.hero-sub{left:783px;top:345px;width:330px;font-size:14px;font-weight:700;color:var(--white);text-transform:uppercase;line-height:19px}
.hero-btn{left:783px;top:397px;width:106px;height:34px;background:var(--blue);border:1px solid var(--white);color:var(--white);font-size:13px;text-transform:uppercase;display:flex;align-items:center;justify-content:center}
.arrow{top:350px;width:32px;height:32px;border-radius:50%;background:rgba(0,0,0,.45);display:flex;align-items:center;justify-content:center}

/* features */
.features{left:98px;top:557px;width:1004px;height:187px;display:flex;box-shadow:0 22px 30px -14px rgba(0,0,0,.35)}
.feature{flex:1;display:flex;gap:22px;padding:38px 26px}
.feature.one{background:var(--blue)}
.feature.two{background:var(--blue-light)}
.feature h3{font-size:17px;font-weight:500;color:var(--white);text-transform:uppercase;margin-bottom:10px}
.feature p{color:#e6eeff;font-size:11px;line-height:16px}

/* welcome */
.welcome-title{left:0;top:812px;width:1200px;text-align:center;font-size:34px;font-weight:400}
.welcome-title span{color:var(--blue)}
.welcome-text{left:180px;top:873px;width:840px;text-align:center}

/* benefits */
.gray-band{left:0;top:960px;width:1200px;height:1500px;background:var(--gray-bg);clip-path:polygon(0 130px,100% 0,100% 100%,0 100%)}
.benefit-title{font-size:28px;font-weight:400;color:var(--ink)}
.benefit-text{width:493px}
.right{text-align:right}
.btn-dark{width:100px;height:32px;border-radius:16px;background:var(--ink);color:var(--white);font-size:12px;display:flex;align-items:center;justify-content:center}
.illus{width:242px;height:242px;border-radius:50%;background:radial-gradient(circle at 50% 55%,#5b8ce0,#3566c8)}
.divider{left:180px;width:840px;height:1px;background:var(--line)}

/* how it works */
.how{left:0;top:2359px;width:1200px;height:645px;background:linear-gradient(180deg,#1b2030,#2a3146 60%,#151a26);clip-path:polygon(0 0,100% 120px,100% 560px,0 645px)}
.how-title{left:0;top:2512px;width:1200px;text-align:center;color:var(--white);font-size:30px;font-weight:400;text-transform:uppercase}
.step-icon{top:2597px;width:88px;height:88px}
.step-text{top:2714px;width:240px;text-align:center;color:var(--white);font-size:13px;line-height:19px}
.dash{top:2630px}
.how-btn{left:504px;top:2820px;width:192px;height:40px;border-radius:20px;background:var(--blue);border:2px solid var(--white);color:var(--white);font-size:15px;font-weight:500;text-transform:uppercase;display:flex;align-items:center;justify-content:center}

/* news */
.news-title{left:0;top:3005px;width:1200px;text-align:center;font-size:30px;font-weight:400;text-transform:uppercase}
.card{top:3097px;width:314px}
.card-photo{height:195px}
.card-date{position:absolute;left:8px;top:225px;width:48px;height:48px;border-radius:50%;background:var(--orange);color:var(--white);font-size:9px;font-weight:700;text-align:center;line-height:11px;display:flex;align-items:center;justify-content:center}
.card-body{padding:22px 0 0 70px;height:104px}
.card-body h4{font-size:15px;font-weight:400;margin-bottom:6px}
.card-body p{font-size:11px;line-height:15px}
.card-rule{height:2px;background:#cccccc}

/* footer */
.footer{left:0;top:3460px;width:1200px;height:373px;background:var(--gray-bg);clip-path:polygon(0 0,100% 90px,100% 100%,0 100%)}
.foot-logo{left:98px;top:3590px;display:flex;align-items:center;gap:10px}
.foot-logo .logo-dot{width:34px;height:34px}
.foot-logo .logo-name{font-size:24px}
.foot-about{left:98px;top:3650px;width:230px;font-size:11px;line-height:16px}
.socials{left:98px;top:3728px;display:flex;gap:6px}
.socials span{width:24px;height:24px;border-radius:50%;border:1px solid var(--ink)}
.foot-h{top:3592px;font-size:16px;font-weight:500;text-transform:uppercase;color:var(--ink)}
.news-p{left:397px;top:3625px;width:240px;font-size:11px;line-height:16px}
.email-box{left:397px;top:3675px;width:245px;height:38px;background:var(--white);border:1px solid var(--line);font-size:11px;color:var(--muted);padding:12px}
.sub-btn{left:397px;top:3728px;width:124px;height:32px;background:var(--blue);color:var(--white);font-size:12px;text-transform:uppercase;display:flex;align-items:center;justify-content:center}
.contact-row{left:713px;display:flex;gap:14px;font-size:12px;color:var(--ink);line-height:17px}
.links{left:995px;top:3632px;list-style:none}
.links li{font-size:12px;line-height:26px;color:var(--ink)}
.copyright{left:0;top:3848px;width:1200px;text-align:center;font-size:11px;color:var(--muted)}
</style>
</head>
<body>

<!-- header -->
<div class="abs phone-tab">
  <svg width="16" height="16" viewBox="0 0 24 24"><circle cx="12" cy="12" r="11" fill="none" stroke="#fff" stroke-width="2"/><path d="M8 6l2 0 1 3-1.5 1a8 8 0 0 0 4 4l1-1.5 3 1v2c0 1-1 2-2 2A10 10 0 0 1 6 8c0-1 1-2 2-2z" fill="#fff"/></svg>
  0400 555 218
</div>
<div class="abs logo"><span class="logo-dot"></span><span class="logo-name">Bright Thrift</span></div>
<nav class="abs nav">
  <a class="active" href="#">Home</a>
  <a href="#" style="margin-left:21px">About Us</a>
  <a href="#" style="margin-left:38px">Our Services</a>
  <a href="#" style="margin-left:36px">How It Works</a>
  <a href="#" style="margin-left:36px">Blog</a>
  <a href="#" style="margin-left:42px">Contact Us</a>
</nav>

<!-- hero -->
<div class="abs hero" role="img" aria-label="Photo of solar panels on a grassy field under a sunny blue sky"></div>
<div class="abs hero-panels" role="img" aria-label="Rows of solar panels in the foreground"></div>
<svg class="abs hero-cut" width="1200" height="448"><polygon points="650,448 1200,380 1200,448" fill="#fff"/></svg>
<div class="abs arrow" style="left:30px"><svg width="12" height="12" viewBox="0 0 12 12"><path d="M8 1L3 6l5 5" stroke="#fff" stroke-width="2" fill="none"/></svg></div>
<div class="abs arrow" style="left:1130px"><svg width="12" height="12" viewBox="0 0 12 12"><path d="M4 1l5 5-5 5" stroke="#fff" stroke-width="2" fill="none"/></svg></div>
<h1 class="abs hero-title">Bright Thrift</h1>
<div class="abs hero-sub">Clean power for your home, install today, start saving from day one</div>
<div class="abs hero-btn">Read More</div>

<!-- features -->
<section class="abs features">
  <div class="feature one">
    <svg width="72" height="60" viewBox="0 0 72 60"><rect x="4" y="4" width="64" height="40" fill="none" stroke="#fff" stroke-width="3"/><path d="M25 4v40M46 4v40M4 24h64M36 44v12M24 56h24" stroke="#fff" stroke-width="3"/></svg>
    <div><h3>Bright Thrift as safe</h3><p>Every system is fitted by accredited installers and checked by the council team, so your home and your savings stay protected for the whole life of the system.</p></div>
  </div>
  <div class="feature two">
    <svg width="64" height="64" viewBox="0 0 64 64"><circle cx="32" cy="32" r="28" fill="none" stroke="#fff" stroke-width="3"/><path d="M18 33l10 10 20-22" stroke="#fff" stroke-width="5" fill="none"/></svg>
    <div><h3>Reliable and trustworthy</h3><p>Backed by local councils and greenhouse alliances, the program offers clear terms, no hidden fees and friendly support whenever you need help with your system.</p></div>
  </div>
</section>

<!-- welcome -->
<h2 class="abs welcome-title">Welcome To <span>Bright Thrift</span></h2>
<p class="abs welcome-text">Bright Thrift is a pioneering approach by councils to support pensioner households to save money and take control of their energy bills by installing affordable, quality solar systems with no upfront costs. Bright Thrift, based on the City of Alderbrook's successful program, ensures that pension card households receive a solar system that pays for itself in electricity savings from day one. Bright Thrift will be progressively</p>

<!-- benefits -->
<div class="abs gray-band"></div>

<h3 class="abs benefit-title" style="left:212px;top:1115px;width:493px;text-align:right">Save money on your energy bills</h3>
<p class="abs benefit-text right" style="left:212px;top:1172px">Solar power cuts the cost of your electricity from the very first day. Repayments are set below the savings you make, so your household budget stays ahead each quarter and you keep more of your pension for the things that matter.</p>
<div class="abs btn-dark" style="left:605px;top:1268px">Read More</div>
<div class="abs illus" style="left:734px;top:1089px" role="img" aria-label="Illustration of a red piggy bank with a coin"></div>
<div class="abs divider" style="top:1369px"></div>

<div class="abs illus" style="left:212px;top:1407px" role="img" aria-label="Illustration of a clipboard bill with a calculator and cash"></div>
<h3 class="abs benefit-title" style="left:487px;top:1432px">Take control of your energy bills</h3>
<p class="abs benefit-text" style="left:487px;top:1490px">See exactly how much power your panels make and how much you use. Simple reports help you plan ahead, avoid bill shock and decide when to run appliances so your solar energy goes further every single day.</p>
<div class="abs btn-dark" style="left:487px;top:1587px">Read More</div>
<div class="abs divider" style="top:1690px"></div>

<h3 class="abs benefit-title" style="left:212px;top:1758px;width:493px;text-align:right">Become more energy independent</h3>
<p class="abs benefit-text right" style="left:212px;top:1815px">Generate your own clean power on your own roof. Relying less on the grid protects you from rising prices and gives you peace of mind, while lowering emissions for your community and the generations that follow you.</p>
<div class="abs btn-dark" style="left:605px;top:1913px">Read More</div>
<div class="abs illus" style="left:726px;top:1731px" role="img" aria-label="Illustration of a solar panel under a sun and cloud"></div>
<div class="abs divider" style="top:2048px"></div>

<div class="abs illus" style="left:212px;top:2087px" role="img" aria-label="Illustration of three solar panels with a bright sun"></div>
<h3 class="abs benefit-title" style="left:487px;top:2110px">It's simple – we've done all the hard work</h3>
<p class="abs benefit-text" style="left:487px;top:2168px">We select trusted installers, quality panels and fair pricing for you. Our team handles the paperwork, approvals and checks, so all you need to do is say yes and start enjoying lower bills from the sun.</p>
<div class="abs btn-dark" style="left:487px;top:2266px">Read More</div>

<!-- how it works -->
<section class="abs how" role="img" aria-label="Dark background photo of solar panels at dusk"></section>
<h2 class="abs how-title">How It Works</h2>

<svg class="abs step-icon" style="left:145px" viewBox="0 0 88 88"><circle cx="44" cy="40" r="36" fill="var(--blue)" stroke="#fff" stroke-width="3"/><path d="M34 74l10 12 10-12" fill="var(--blue)"/><circle cx="44" cy="32" r="8" fill="#fff"/><path d="M30 54a14 12 0 0 1 28 0z" fill="#fff"/></svg>
<svg class="abs step-icon" style="left:417px" viewBox="0 0 88 88"><circle cx="44" cy="40" r="36" fill="var(--blue)" stroke="#fff" stroke-width="3"/><path d="M34 74l10 12 10-12" fill="var(--blue)"/><circle cx="44" cy="40" r="14" fill="none" stroke="#fff" stroke-width="3"/><circle cx="44" cy="40" r="4" fill="#fff"/></svg>
<svg class="abs step-icon" style="left:692px" viewBox="0 0 88 88"><circle cx="44" cy="40" r="36" fill="var(--blue)" stroke="#fff" stroke-width="3"/><path d="M34 74l10 12 10-12" fill="var(--blue)"/><rect x="26" y="26" width="36" height="22" fill="none" stroke="#fff" stroke-width="2.5"/><path d="M38 26v22M50 26v22M26 37h36M44 48v8M36 56h16" stroke="#fff" stroke-width="2.5"/></svg>
<svg class="abs step-icon" style="left:972px" viewBox="0 0 88 88"><circle cx="44" cy="40" r="36" fill="var(--blue)" stroke="#fff" stroke-width="3"/><path d="M34 74l10 12 10-12" fill="var(--blue)"/><rect x="24" y="29" width="40" height="22" rx="2" fill="none" stroke="#fff" stroke-width="2.5"/><circle cx="44" cy="40" r="6" fill="#fff"/></svg>

<svg class="abs dash" style="left:292px" width="110" height="20"><path d="M2 14 Q55 0 100 10" stroke="#fff" stroke-width="2" stroke-dasharray="6 5" fill="none"/><path d="M96 4l8 6-9 4" stroke="#fff" stroke-width="2" fill="none"/></svg>
<svg class="abs dash" style="left:568px" width="110" height="20"><path d="M2 14 Q55 0 100 10" stroke="#fff" stroke-width="2" stroke-dasharray="6 5" fill="none"/><path d="M96 4l8 6-9 4" stroke="#fff" stroke-width="2" fill="none"/></svg>
<svg class="abs dash" style="left:840px" width="110" height="20"><path d="M2 14 Q55 0 100 10" stroke="#fff" stroke-width="2" stroke-dasharray="6 5" fill="none"/><path d="M96 4l8 6-9 4" stroke="#fff" stroke-width="2" fill="none"/></svg>

<p class="abs step-text" style="left:69px">Bright Thrift checks that every person gets a solar system that pays for itself in energy savings from day one</p>
<p class="abs step-text" style="left:341px">Bright Thrift organises for the solar system to be installed</p>
<p class="abs step-text" style="left:616px">Bright Thrift supports pensioners to understand and get the most out of solar</p>
<p class="abs step-text" style="left:896px">Pensioners gradually pay for cost through their usual rates payments at 0% interest</p>
<div class="abs how-btn">Get Involved</div>

<!-- news -->
<h2 class="abs news-title">Latest News</h2>
<article class="abs card" style="left:101px">
  <div class="card-photo" role="img" aria-label="Photo of a field of solar panels at sunset" style="background:linear-gradient(180deg,#f3c46a,#8aa6c8 50%,#2f4f8a)"></div>
  <div class="card-date">APR 05<br>2017</div>
  <div class="card-body"><h4>Nemo enim ipsam voluptatem</h4><p>Sed ut perspiciatis unde omnis iste natus error sit voluptatem accusantium</p></div>
  <div class="card-rule"></div>
</article>
<article class="abs card" style="left:443px">
  <div class="card-photo" role="img" aria-label="Illustration of wind turbines and solar panels with a green plug" style="background:linear-gradient(180deg,#6fb4e8,#9fd0f0 45%,#5aa84a)"></div>
  <div class="card-date">APR 05<br>2017</div>
  <div class="card-body"><h4>Nemo enim ipsam voluptatem</h4><p>Sed ut perspiciatis unde omnis iste natus error sit voluptatem accusantium</p></div>
  <div class="card-rule"></div>
</article>
<article class="abs card" style="left:788px">
  <div class="card-photo" role="img" aria-label="Photo of a technician in a hard hat inspecting solar panels" style="background:linear-gradient(135deg,#bfe3f7,#4aa0de 60%,#2e6fb8)"></div>
  <div class="card-date">APR 05<br>2017</div>
  <div class="card-body"><h4>Nemo enim ipsam voluptatem</h4><p>Sed ut perspiciatis unde omnis iste natus error sit voluptatem accusantium</p></div>
  <div class="card-rule"></div>
</article>

<!-- footer -->
<footer class="abs footer"></footer>
<div class="abs foot-logo"><span class="logo-dot"></span><span class="logo-name">Bright Thrift</span></div>
<p class="abs foot-about">Nemo enim ipsam voluptatem quia voluptas sit aspernatur aut odit aut fugit, sed quia consequuntur magni dolores</p>
<div class="abs socials"><span></span><span></span><span></span><span></span></div>

<h4 class="abs foot-h" style="left:397px">Sign Up For Newsletter</h4>
<p class="abs news-p">Excepteur sint occaecat cupidatat non proident, sunt in culpa qui officia deserunt</p>
<div class="abs email-box">Enter email</div>
<div class="abs sub-btn">Subscription</div>

<h4 class="abs foot-h" style="left:713px">Contact Us</h4>
<div class="abs contact-row" style="top:3632px">
  <svg width="12" height="16" viewBox="0 0 12 16"><path d="M6 0a6 6 0 0 1 6 6c0 4-6 10-6 10S0 10 0 6a6 6 0 0 1 6-6z" fill="var(--ink)"/><circle cx="6" cy="6" r="2.2" fill="#f3f3f3"/></svg>
  <span>Bright Thrift 12 Wattle Lane,<br>Alderbrook VIC 3999</span>
</div>
<div class="abs contact-row" style="top:3690px">
  <svg width="14" height="14" viewBox="0 0 24 24"><path d="M5 2h4l2 5-3 2a12 12 0 0 0 7 7l2-3 5 2v4c0 1-1 3-3 3A19 19 0 0 1 2 5c0-2 2-3 3-3z" fill="var(--ink)"/></svg>
  <span>Phone:&nbsp; 0400 555 218</span>
</div>
<div class="abs contact-row" style="top:3727px">
  <svg width="14" height="12" viewBox="0 0 14 12"><rect x="0.5" y="0.5" width="13" height="11" fill="none" stroke="var(--ink)"/><path d="M1 1l6 5 6-5" stroke="var(--ink)" fill="none"/></svg>
  <span>ned.lowe@brightthrift.example</span>
</div>

<h4 class="abs foot-h" style="left:995px">Quick Links</h4>
<ul class="abs links">
  <li>Home</li><li>About Us</li><li>Services</li><li>Get A Quote</li><li>Blog</li><li>Contact Us</li>
</ul>

<div class="abs copyright">©2017 Bright Thrift., All Rights Reserved.</div>

</body>
</html>
```